Muslim funeral brochure for Swedish market

Purpose of the brochure: We are a new funeral home in Sweden. We are launching a funeral guide for muslim funerals in Sweden in order to develop credibility. We will create a brochure that describe how a muslim funeral is conducted in Sweden and aspects that are important for the relatives of the deceased to understand.

Size of the brochure: We are hoping that muslim associations in Sweden will have our brochure on their website and that they should have a link from where the brochure should be downloaded. Is should be possible to print the brochure on a regular printer. We will most likely print the brochure and for this purpose it would be helpful if the brochure is constructed in an attractive format.

Content: We have attached a preliminary text intended for our brochure. The attached pdf is not indicative for how we would like the end product to look like.

This URL:

http://blogg.vardagsnytt-exempel.se/lindaq/files/2013/11/infographic-trollvik.jpeg-page.jpg

goes to a brochure we found on the web that describes child car safety that a company is using to get authority to sell more car seats (maybe we can use this for inspiration)
Updates

Please note that the design in the pdf I attached to the project brief should not be indicative for how I would like the end product to look like. It is a scetch I did to communicate content to the designers of pixel guild. I am hoping for a more appealing design eg the URL I attached in the brief is a good example of how a boring subject was communicated in an appealing way.Thanks Torsten Added Friday, October 30, 2015

Target Market(s)

Muslims in Sweden

Industry/Entity Type

Funeral Home

Font styles to use
Sans Serif

Colors
00a990

Requirements
Must have
• *Relevant illustrations
• *Enough space so that we can translate into several languages without changing design
• *A format that we ourselves can change in case needed
• *Brochure use same colors and design (if possible and unless the designer has some better ideas) as we do on our web page www.ljunggravning-exempel.se.
• *Should be possible to create a print friendly version of the flyer with less colors
Nice to have
• Suggestions of which brochure formats we should use in order to make it:
• *Attractive for professional print
• *Print friendly format for home users
Should not have
• Symbols specific to a certain fraction of islam e.g. sunni, shia muslim and ISIS

```html
<!DOCTYPE html>
<html lang="sv">
<head>
<meta charset="utf-8">
<title>Så utförs en muslimsk begravning i Sverige</title>
<link href="https://fonts.googleapis.com/css2?family=Montserrat:wght@600;700&family=Nunito+Sans:wght@400;600;700&display=swap" rel="stylesheet">
<style>
  :root{
    --teal-dark:#1f5b63;
    --teal-heading:#1d6069;
    --ink:#2a2a2a;
    --page:#ffffff;
    --backdrop:#f1f1f1;
    --chevron-light:#f7f7f7;
    --chevron-dark:#e1e1e1;
  }
  *{box-sizing:border-box;margin:0;padding:0}
  html,body{width:1200px;height:1200px;overflow:hidden;background:var(--backdrop)}
  body{font-family:"Nunito Sans",Arial,sans-serif;color:var(--ink)}
  .flyer{position:absolute;left:176px;top:0;width:848px;height:1200px;background:var(--page);box-shadow:0 0 18px rgba(0,0,0,.12)}
  .flyer-header{position:absolute;left:0;top:0;width:100%;height:94px;background:var(--teal-dark);display:flex;align-items:center;padding-left:53px}
  .flyer-title{font-family:"Montserrat",Arial,sans-serif;font-weight:700;font-size:29px;color:#fff;letter-spacing:.2px}
  .header-emblem{position:absolute;right:38px;top:18px;width:60px;height:60px;border-radius:50%;background:radial-gradient(circle at 40% 40%,#ffffff 0,#dfe9ea 70%)}
  .intro{position:absolute;left:51px;top:106px;width:760px;font-size:13.3px;line-height:18.8px;text-transform:uppercase;letter-spacing:.1px}
  .timeline-label{position:absolute;right:79px;top:187px;font-family:"Montserrat",Arial,sans-serif;font-weight:600;font-size:27px;letter-spacing:3px;color:#222}
  .timeline-band{position:absolute;left:51px;top:220px;width:760px;height:104px}
  .step-art{position:absolute;border-radius:4px}
  .art-home{left:0;top:40px;width:84px;height:64px;background:linear-gradient(#5b5470,#b9bcc0 55%,#69b86b)}
  .art-hospital{left:256px;top:22px;width:100px;height:82px;background:linear-gradient(#9ed3d7,#7fbfc5 70%,#5a6770)}
  .art-mosque{left:504px;top:28px;width:150px;height:76px;background:linear-gradient(#8fd0da,#2c6d9c 55%,#1c2e57)}
  .steps{position:absolute;left:51px;top:345px;width:760px}
  .step-text{position:absolute;top:0;font-size:14px;line-height:18.9px}
  .step-1{left:0;width:190px}
  .step-2{left:252px;width:215px}
  .step-3{left:516px;width:225px}
  .info{position:absolute;left:51px;top:504px;width:775px;display:flex;flex-direction:column;gap:8.5px}
  .info-block{font-size:14px;line-height:18.9px}
  .info-heading{font-family:"Montserrat",Arial,sans-serif;font-weight:600;font-size:18.5px;color:var(--teal-heading);text-transform:uppercase;letter-spacing:.1px}
  .flyer-footer{position:absolute;left:0;bottom:0;width:100%;height:107px;background:var(--teal-dark);color:#fff}
  .footer-url{position:absolute;left:57px;top:14px;font-family:"Montserrat",Arial,sans-serif;font-weight:700;font-size:27px;letter-spacing:2.4px}
  .footer-contact{position:absolute;left:50px;top:62px;display:flex;align-items:center;gap:10px;font-family:"Montserrat",Arial,sans-serif;font-weight:700;font-size:18px;letter-spacing:1.4px}
  .footer-contact svg{flex:none}
  .contact-gap{width:18px}
  .brand-name{position:absolute;right:40px;top:38px;font-family:"Montserrat",Arial,sans-serif;font-weight:700;font-size:36px;letter-spacing:4px;color:#fff}
</style>
</head>
<body>
<main class="flyer">
  <header class="flyer-header">
    <h1 class="flyer-title">Så utförs en muslimsk begravning i Sverige</h1>
    <div class="header-emblem" role="img" aria-label="Halvmåne med stjärna"></div>
  </header>

  <p class="intro">Muslimer kommer från olika länder, har skilda språk och olika kulturbakgrund. Därför kan det finnas olika församlingar där regler och traditioner i samband med begravning skiljer sig åt. Muslimer skall alltid jordbegravas och begravningsplatsens gravar skall läggas så att den döde ligger vänd mot Mekka.</p>

  <div class="timeline-label">INOM 36 TIMMAR</div>

  <div class="timeline-band">
    <svg width="760" height="104" viewBox="0 0 760 104" aria-hidden="true">
      <defs>
        <linearGradient id="chev" x1="0" x2="1">
          <stop offset="0" stop-color="#ffffff"/>
          <stop offset="1" stop-color="#dcdcdc"/>
        </linearGradient>
      </defs>
      <polygon points="0,0 117,0 150,52 117,104 0,104" fill="url(#chev)"/>
      <polygon points="150,0 398,0 430,52 398,104 150,104 182,52" fill="url(#chev)"/>
      <polygon points="430,0 722,0 755,52 722,104 430,104 462,52" fill="url(#chev)"/>
    </svg>
    <div class="step-art art-home" role="img" aria-label="Illustration av ett bostadshus"></div>
    <div class="step-art art-hospital" role="img" aria-label="Illustration av ett sjukhus"></div>
    <div class="step-art art-mosque" role="img" aria-label="Illustration av en moské"></div>
  </div>

  <section class="steps">
    <p class="step-text step-1">Inträffar dödsfallet i t.ex. hemmet eller på ålderdomshem transporteras kroppen till ett sjukhus.</p>
    <p class="step-text step-2">Dödsorsak fastställs och innan kroppen lämnar bårhuset genomförs en religiös tvagningsceremoni varefter den döde lindas i bomullstyg. Under ceremonin deltar en Imam samt en representant från begravningsbyrån.</p>
    <p class="step-text step-3">Begravningen sker efter middagsbönen. Den inleds med en kort bön ochsedan följer männen med till begravning­splatsen. De hjälps åt att lägga den döde i graven. Kvinnor är som regel inte närvarande utan ber i hemmet.</p>
  </section>

  <section class="info">
    <p class="info-block"><span class="info-heading">Begravning inom 36 timmar</span> - Enligt islam skall den döde begravas så snart som möjligt - helst inom 36 timmar. På grund av de administrativa handläggningstiderna i Sverige är det inte alltid möjligt att utföra begravningen inom 36 timmar. För att möjliggöra så snabb handläggning som möjligt kan anhöriga be jourhav­ande läkare att utfärda och skicka dödsintyg till skatteverket så snabbt som möjligt då de vill begrava den avlidne enligt muslimsk sed dvs. inom 36 timmar. Dödsintyget är nödvändigt för att begravningsbyrån ska kunna beställa ett gravsättningsintyg.</p>
    <p class="info-block"><span class="info-heading">En enkel kista</span> - I muslimska länder är det vanligt att den avlidne begravs utan kista och endast inlindad i bomullstyg. I samband med en jordbegravning i Sverige måste den avlidne ligga i en kista. Vid muslimska begravningar i Sverige väljs därför oftast en mycket enkelt utformad kista.</p>
    <p class="info-block"><span class="info-heading">Din islamiska församling</span> - De flesta utövare av islam i Sverige tillhör en Islamisk församling. Din församling tillhandahåller en Imam som deltar vid den religiösa tvagningsceremonin. I vissa fall kan anhöriga själva tvaga den avlidne. Församlingen brukar dessutom tillhandahålla en Imam som leder begravningsceremonin vid gravplatsen. Det är inte alltid samma Imam som deltar vid tvagnings- och begravningsceremonin.</p>
    <p class="info-block"><span class="info-heading">Din begravningsbyrå</span> - Din begravningsbyrå ansvarar för att samordna transporter och tillhandahåller en enkel kista som den avlidne kan läggas och begravas i. De flesta bårhus kräver att en representant från begravningsbyrån deltar under den religiösa tvagningsceremonin. I de flesta fall ansvarar begravningsbyrån även för att ordna en gravplats för den avlidne. I vissa fall föredrar de anhöriga att själva ordna en gravplats.</p>
    <p class="info-block"><span class="info-heading">Gravplats</span> - Begravningsplatsens gravar skall läggas så att den döde ligger vänd mot Mekka. Graven skall markeras med en enkel gravmarkör som visar var gravens huvud respektive fotändan finns. En mus­limsk grav ska ej beträdas och får inte återanvändas.</p>
    <p class="info-block"><span class="info-heading">Utlandsbegravningar</span> - Om man bestämmer sig för att den avlidne ska begravas utomlands tillkommer en del administration och arbete. Intyg som måste sammanställas inkluderar bland annat dödsfalls-, dödsorsaks- och gravsättningsintyg samt balsamerings-, lödnings-, och transportintyg. I tillägg krävs stämplar från konsulatet vilket hanteras av de anhöriga. Din begravningsbyrå hjälper dig med alla nödvändiga handl­ingar, kontakter med läkare, skatteverket samt ordnar med transporter från sjukhuset till flygplatsen och ordnar transport med flyg. Din begravningsbyrå ordnar även en enkel träkista, zinkkista och flygemballage.</p>
  </section>

  <footer class="flyer-footer">
    <div class="footer-url">www.ljunggravning-exempel.se.</div>
    <div class="footer-contact">
      <svg width="28" height="28" viewBox="0 0 28 28" aria-hidden="true"><circle cx="14" cy="14" r="12.5" fill="none" stroke="#fff" stroke-width="1.6"/><path d="M10 8c-1 1-1.5 2.5-.5 5s3 5 5.5 6.5c1.5.8 3 .8 4-.2l-2.2-2.3-1.6 1c-1.5-.8-3.2-2.6-4-4.3l1.1-1.5z" fill="#fff"/></svg>
      <span>020.41.63.90</span>
      <span class="contact-gap"></span>
      <svg width="30" height="26" viewBox="0 0 30 26" aria-hidden="true"><path d="M3 10 15 2l12 8v14H3z" fill="none" stroke="#fff" stroke-width="1.6"/><path d="M3 10l12 8 12-8" fill="none" stroke="#fff" stroke-width="1.6"/></svg>
      <span>kund@ljunggravning-exempel.se</span>
    </div>
    <div class="brand-name">LJUNG</div>
  </footer>
</main>
</body>
</html>
```